Kovrilex - presentation for a remote DBA team offering data platform management

We need a website design for wordpress site called Kovrilex.cz
We deliver remote database and data platform administration and development, oversee the database administrators, consult and train the personnel responsible for the database operations. The website should include several sections, home page with graphics elements supporting the name and service - remote dba work; blog section; service introduction and description, team introduction and description, download section for documents, presentations etc.

Target Market(s)

small and medium business companies requiring remote DBA service

Number of Pages Required

3 page

Font styles to use
Sans Serif

Colors

Designer to choose colors to be used in the design.

Requirements
Must have
• The website should have several sections to introduce the services, blog, team introduction, downloads

```html
<!DOCTYPE html>
<html lang="en">
<head>
<meta charset="utf-8">
<title>Kovrilex – Remote Database Administration</title>
<link href="https://fonts.googleapis.com/css2?family=Montserrat:wght@500;600;700;800&family=Open+Sans:wght@400;600;700&family=Jost:wght@400;500&display=swap" rel="stylesheet">
<style>
:root{
  --navy:#17306b;
  --ink:#1f2a3c;
  --blue:#1565d8;
  --blue-mid:#1f7fe0;
  --cyan:#22b0d6;
  --text:#6b7280;
  --white:#ffffff;
  --footer-a:#0b3aa8;
  --footer-b:#1c78d8;
  --footer-bar:#0a2b73;
}
*{box-sizing:border-box;margin:0;padding:0}
html,body{width:1200px;height:3409px;overflow:hidden}
body{position:relative;background:var(--white);font-family:"Open Sans",Arial,sans-serif;color:var(--text)}
.abs{position:absolute}
.btn{position:absolute;display:flex;align-items:center;justify-content:center;border:2px solid var(--blue-mid);border-radius:30px;color:var(--navy);font-family:"Montserrat",Arial,sans-serif;font-weight:700;letter-spacing:.5px;background:var(--white)}
.connector{position:absolute;width:18px;height:18px;border:3px solid var(--blue);border-radius:50%;background:var(--white)}
.arrow{position:absolute}

/* hero */
.hero{position:absolute;left:0;top:0;width:1200px;height:618px;overflow:hidden}
.logo{left:182px;top:32px;font-family:"Montserrat",Arial,sans-serif;font-weight:800;font-size:31px;color:var(--navy);letter-spacing:-.5px}
.nav{top:44px;font-family:"Montserrat",Arial,sans-serif;font-weight:600;font-size:13.5px;color:var(--navy)}
.nav.light{color:var(--white)}
.hero-visual{left:580px;top:80px;width:470px;height:440px;border-radius:50%;background:radial-gradient(ellipse at 50% 50%,rgba(233,243,255,.85) 0%,rgba(120,170,235,.55) 40%,rgba(40,110,220,0) 72%)}
.hero-title{left:177px;top:206px;font-family:"Montserrat",Arial,sans-serif;font-weight:800;font-size:32px;line-height:41px;color:var(--navy)}
.hero-title span{color:var(--blue-mid)}
.hero-text{left:182px;top:352px;width:380px;font-size:15.5px;line-height:22px}

/* about */
.about-visual{left:190px;top:650px;width:370px;height:370px;border-radius:50%;background:radial-gradient(circle at 50% 50%,#cfe5f8 0%,#e4f1fb 45%,rgba(255,255,255,0) 70%)}
.about-title{left:623px;top:710px;font-family:"Montserrat",Arial,sans-serif;font-weight:800;font-size:32px;color:var(--ink)}
.about-title span{color:var(--blue-mid)}
.about-text{left:624px;width:415px;font-size:14px;line-height:21px}

/* services */
.services{position:absolute;left:0;top:1086px;width:1200px;height:494px;background:linear-gradient(100deg,#1561f0 0%,#1a7de4 50%,#179fc0 100%)}
.section-title-light{position:absolute;width:1200px;text-align:center;font-family:"Montserrat",Arial,sans-serif;font-weight:700;font-size:27px;color:var(--white)}
.service-card{position:absolute;top:125px;width:267px;height:278px;border:1.5px solid rgba(255,255,255,.7)}
.service-card svg{position:absolute;left:30px;top:20px}
.service-card h3{position:absolute;left:30px;top:92px;font-family:"Montserrat",Arial,sans-serif;font-weight:600;font-size:17px;line-height:24px;color:var(--white)}
.service-card p{position:absolute;left:30px;top:152px;width:215px;font-size:12.5px;line-height:16px;color:rgba(255,255,255,.9)}
.service-card .btn{left:30px;top:215px;width:119px;height:31px;font-size:10px;border:none}

/* team */
.section-title{position:absolute;width:1200px;text-align:center;font-family:"Montserrat",Arial,sans-serif;font-weight:800;font-size:31px;color:var(--ink)}
.section-title span{color:var(--blue-mid)}
.member{position:absolute;top:1734px;width:280px;text-align:center}
.member svg{display:block;margin:0 auto}
.member .name{margin-top:18px;font-family:"Jost",Arial,sans-serif;font-size:23px;color:var(--blue-mid)}
.member .role{margin-top:2px;font-family:"Jost",Arial,sans-serif;font-weight:500;font-size:15px;color:var(--blue-mid)}
.member .bio{width:228px;margin:4px auto 0;font-size:13px;line-height:19px}
.member .more{margin-top:5px;font-family:"Montserrat",Arial,sans-serif;font-weight:700;font-size:13px;color:var(--navy)}

/* blogs */
.blogs{position:absolute;left:0;top:2164px;width:1200px;height:484px;background:linear-gradient(90deg,#f0f0f1,#e9e9ea)}
.blogs-title{left:175px;top:62px;font-family:"Montserrat",Arial,sans-serif;font-weight:700;font-size:27px;color:var(--ink)}
.post{position:absolute;top:116px;width:266px}
.post .thumb{width:266px;height:157px}
.post .date{position:absolute;left:21px;top:141px;width:120px;height:25px;background:var(--blue-mid);color:var(--white);font-size:12px;display:flex;align-items:center;justify-content:center}
.post h4{margin-top:22px;font-family:"Montserrat",Arial,sans-serif;font-weight:700;font-size:12.5px;line-height:18px;color:var(--ink)}
.post p{margin-top:6px;font-size:9.5px;line-height:13.5px}
.post .more{margin-top:10px;font-family:"Montserrat",Arial,sans-serif;font-weight:700;font-size:11px;color:var(--blue)}

/* downloads */
.dl-title{position:absolute;top:2702px;width:1200px;text-align:center;font-family:"Montserrat",Arial,sans-serif;font-weight:700;font-size:21px;color:var(--blue-mid)}
.dl-title span{color:var(--cyan)}
.dl-shadow{position:absolute;width:389px;height:191px;border:6px solid #dbeaf6;border-top:none;border-right:none}
.dl-card{position:absolute;top:2768px;width:390px;height:191px;background:var(--white);box-shadow:0 4px 18px rgba(30,60,110,.16)}
.dl-card .doc{position:absolute;left:32px;top:28px;width:94px;height:136px}
.dl-card h4{position:absolute;left:160px;top:36px;font-family:"Montserrat",Arial,sans-serif;font-weight:600;font-size:17px;color:var(--blue-mid)}
.dl-card p{position:absolute;left:160px;top:64px;width:205px;font-size:11px;line-height:14px}
.dl-card .btn{left:157px;top:121px;width:130px;height:37px;font-size:11px;border-width:1.5px}

/* footer */
.footer{position:absolute;left:0;top:3057px;width:1200px;height:289px;background:linear-gradient(100deg,var(--footer-a),var(--footer-b))}
.f-col{position:absolute;top:70px;color:var(--white)}
.f-col h5{font-family:"Montserrat",Arial,sans-serif;font-weight:600;font-size:17px;margin-bottom:12px;letter-spacing:.3px}
.f-col li{list-style:none;font-size:14px;line-height:29.5px;color:rgba(255,255,255,.85);display:flex;align-items:center;gap:8px}
.f-bar{position:absolute;left:0;top:3346px;width:1200px;height:63px;background:var(--footer-bar);color:rgba(255,255,255,.75);font-size:13px;display:flex;align-items:center;justify-content:center}
</style>
</head>
<body>

<section class="hero">
  <svg class="abs" style="left:0;top:0" width="1200" height="618" viewBox="0 0 1200 618">
    <defs>
      <linearGradient id="heroBlue" x1="0" y1="0" x2="1" y2="1">
        <stop offset="0" stop-color="#2ac6d6"/>
        <stop offset=".45" stop-color="#1d8fe2"/>
        <stop offset="1" stop-color="#1457e0"/>
      </linearGradient>
    </defs>
    <path d="M 925 0 C 895 40, 615 150, 562 330 C 540 450, 558 560, 590 618 L 1200 618 L 1200 0 Z" fill="#cfe6f5"/>
    <path d="M 960 0 C 930 40, 650 150, 600 330 C 580 450, 600 560, 640 618 L 1200 618 L 1200 0 Z" fill="url(#heroBlue)"/>
  </svg>
  <div class="abs hero-visual" role="img" aria-label="Isometric illustration of database server racks beside an open laptop"></div>
  <div class="abs logo">Kovrilex</div>
  <div class="abs nav" style="left:441px">ABOUT US</div>
  <div class="abs nav" style="left:541px">SERVICES</div>
  <div class="abs nav" style="left:639px">BLOGS</div>
  <div class="abs nav" style="left:716px">TEAM</div>
  <div class="abs nav" style="left:788px">RESOURCES</div>
  <div class="abs nav light" style="left:902px">CONTACT US</div>

  <h1 class="abs hero-title">REMOTE DATABASE<br><span>&amp; DATA PLATFORM<br>ADMINISTRATION</span></h1>
  <p class="abs hero-text">Maecenas aliquet velit vel turpis Mauris neque metus malesuada nec ultricies sit amet</p>
  <a class="btn" style="left:173px;top:413px;width:164px;height:48px;font-size:13px">READ MORE</a>

  <svg class="arrow" style="left:78px;top:280px" width="32" height="56" viewBox="0 0 32 56"><path d="M28 3 L5 28 L28 53" fill="none" stroke="#9aa3ad" stroke-width="2.5"/></svg>
  <svg class="arrow" style="left:1098px;top:280px" width="32" height="56" viewBox="0 0 32 56"><path d="M4 3 L27 28 L4 53" fill="none" stroke="#ffffff" stroke-width="2.5"/></svg>
</section>

<section>
  <div class="abs about-visual" role="img" aria-label="Isometric illustration of a cloud linked to laptop, monitor, tablet and phone"></div>
  <h2 class="abs about-title">ABOUT <span>KOVRILEX</span></h2>
  <p class="abs about-text" style="top:772px">Maecenas aliquet velit vel turpis Mauris neque metus malesuada nec ultricies sit amet porttitor</p>
  <p class="abs about-text" style="top:838px">Aed nulla In ullamcorper est eget tempor cursus neque mi consectetuer mi a ultricies massa est sed nisl Class aptent taciti sociosqu ad litora torquent per</p>
  <a class="btn" style="left:623px;top:932px;width:164px;height:48px;font-size:13px">READ MORE</a>
  <div class="abs" style="left:606px;top:1020px;width:2px;height:58px;background:#b7c6d8"></div>
  <div class="connector" style="left:598px;top:1070px"></div>
</section>

<section class="services">
  <h2 class="section-title-light" style="top:52px">OUR SERVICES</h2>

  <div class="service-card" style="left:180px">
    <svg width="70" height="60" viewBox="0 0 70 60" fill="none" stroke="#fff" stroke-width="2">
      <path d="M16 40 H54 a12 12 0 0 0 0 -24 a16 16 0 0 0 -30 -2 a12 12 0 0 0 -8 26 Z"/>
      <ellipse cx="35" cy="30" rx="9" ry="3"/><path d="M26 30 V40 M44 30 V40"/>
      <path d="M35 40 V56 M22 56 H48"/>
    </svg>
    <h3>REMOTE<br>DATABASE</h3>
    <p>Maecenas aliquet velit vel turpis Mauris neque metus malesuada nec ultricies sit amet</p>
    <a class="btn">READ MORE</a>
  </div>

  <div class="service-card" style="left:464px">
    <svg width="70" height="60" viewBox="0 0 70 60" fill="none" stroke="#fff" stroke-width="2">
      <circle cx="22" cy="14" r="7"/><circle cx="48" cy="14" r="7"/>
      <path d="M10 36 a12 12 0 0 1 24 0 M36 36 a12 12 0 0 1 24 0"/>
      <path d="M35 36 V46 M18 46 H52 M18 46 V56 M52 46 V56"/>
    </svg>
    <h3>CONSULT<br>AND TRAIN</h3>
    <p>Maecenas aliquet velit vel turpis Mauris neque metus malesuada nec ultricies sit amet</p>
    <a class="btn">READ MORE</a>
  </div>

  <div class="service-card" style="left:748px">
    <svg width="70" height="60" viewBox="0 0 70 60" fill="none" stroke="#fff" stroke-width="2">
      <circle cx="35" cy="26" r="17" stroke-dasharray="6 3"/>
      <path d="M35 17 a9 9 0 0 0 -5 16 V38 H40 V33 a9 9 0 0 0 -5 -16 Z"/>
      <path d="M31 43 H39 M32 48 H38"/>
    </svg>
    <h3>ADMINISTRATION<br>AND DEVELOPMENT</h3>
    <p>Maecenas aliquet velit vel turpis Mauris neque metus malesuada nec ultricies sit amet</p>
    <a class="btn">READ MORE</a>
  </div>
</section>
<div class="abs" style="left:598px;top:1564px;width:2px;height:50px;background:#b7c6d8"></div>
<div class="connector" style="left:590px;top:1612px"></div>

<section>
  <h2 class="section-title" style="top:1667px">OUR <span>TEAM</span></h2>
  <svg class="arrow" style="left:160px;top:1826px" width="20" height="32" viewBox="0 0 20 32"><path d="M17 2 L3 16 L17 30" fill="none" stroke="#b0b6bd" stroke-width="2.5"/></svg>
  <svg class="arrow" style="left:1015px;top:1826px" width="20" height="32" viewBox="0 0 20 32"><path d="M3 2 L17 16 L3 30" fill="none" stroke="#b0b6bd" stroke-width="2.5"/></svg>

  <div class="member" style="left:162px">
    <svg width="180" height="196" viewBox="0 0 180 196" role="img" aria-label="Portrait photo of team member">
      <polygon points="90,2 170,48 170,148 90,194 10,148 10,48" fill="none" stroke="#2a86c8" stroke-width="2"/>
      <polygon points="90,14 160,54 160,142 90,182 20,142 20,54" fill="#b08a73"/>
    </svg>
    <div class="name">Member Name</div>
    <div class="role">Designation</div>
    <p class="bio">Class aptent taciti sociosqu ad litora torquent per conubia nosMaecenas aliquet velit vel turpis Mauris</p>
    <div class="more">READ MORE</div>
  </div>
  <div class="member" style="left:458px">
    <svg width="180" height="196" viewBox="0 0 180 196" role="img" aria-label="Portrait photo of team member">
      <polygon points="90,2 170,48 170,148 90,194 10,148 10,48" fill="none" stroke="#2a86c8" stroke-width="2"/>
      <polygon points="90,14 160,54 160,142 90,182 20,142 20,54" fill="#4a3a34"/>
    </svg>
    <div class="name">Member Name</div>
    <div class="role">Designation</div>
    <p class="bio">Class aptent taciti sociosqu ad litora torquent per conubia nosMaecenas aliquet velit vel turpis Mauris</p>
    <div class="more">READ MORE</div>
  </div>
  <div class="member" style="left:751px">
    <svg width="180" height="196" viewBox="0 0 180 196" role="img" aria-label="Portrait photo of team member">
      <polygon points="90,2 170,48 170,148 90,194 10,148 10,48" fill="none" stroke="#2a86c8" stroke-width="2"/>
      <polygon points="90,14 160,54 160,142 90,182 20,142 20,54" fill="#9c7a62"/>
    </svg>
    <div class="name">Member Name</div>
    <div class="role">Designation</div>
    <p class="bio">Class aptent taciti sociosqu ad litora torquent per conubia nosMaecenas aliquet velit vel turpis Mauris</p>
    <div class="more">READ MORE</div>
  </div>
</section>

<section class="blogs">
  <div class="abs" style="left:598px;top:-20px;width:2px;height:34px;background:#b7c6d8"></div>
  <div class="connector" style="left:590px;top:10px"></div>
  <h2 class="abs blogs-title">RECENT BLOGS</h2>

  <article class="post" style="left:177px">
    <div class="thumb" role="img" aria-label="Photo of hands typing code on a laptop" style="background:linear-gradient(135deg,#6b6e72,#3b3d40)"></div>
    <div class="date">02 May 2018</div>
    <h4>Praesent elementum elit at tellus nec ultricies sit amet porttito</h4>
    <p>Donec quis massa et lacus tempor gravida nunc vel nibh integer quis urna at ante enim dapibus ultrices</p>
    <div class="more">READ MORE</div>
  </article>
  <article class="post" style="left:468px">
    <div class="thumb" role="img" aria-label="Photo of program code on a dark screen" style="background:linear-gradient(135deg,#2a2c33,#15161a)"></div>
    <div class="date">02 May 2018</div>
    <h4>Praesent elementum elit at tellus nec ultricies sit amet porttito</h4>
    <p>Donec quis massa et lacus tempor gravida nunc vel nibh integer quis urna at ante enim dapibus ultrices</p>
    <div class="more">READ MORE</div>
  </article>
  <article class="post" style="left:761px">
    <div class="thumb" role="img" aria-label="Photo of an engineer with a tablet in a server room" style="background:linear-gradient(135deg,#2d4e8c,#1a2a52 60%,#c88d8a)"></div>
    <div class="date">02 May 2018</div>
    <h4>Praesent elementum elit at tellus nec ultricies sit amet porttito</h4>
    <p>Donec quis massa et lacus tempor gravida nunc vel nibh integer quis urna at ante enim dapibus ultrices</p>
    <div class="more">READ MORE</div>
  </article>
</section>

<section>
  <div class="abs" style="left:598px;top:2648px;width:2px;height:16px;background:#b7c6d8"></div>
  <div class="connector" style="left:590px;top:2662px"></div>
  <h2 class="dl-title">DOWNLOAD <span>RESOURCES</span></h2>

  <div class="abs" style="left:-10px;top:2798px;width:108px;height:160px;background:var(--white);box-shadow:0 4px 14px rgba(30,60,110,.12);border-bottom:5px solid #dbeaf6"></div>
  <div class="abs" style="left:0;top:2818px;font-family:Montserrat,Arial,sans-serif;font-weight:600;font-size:15px;color:var(--blue-mid)">Title</div>
  <div class="abs" style="left:1073px;top:2782px;width:140px;height:166px;background:var(--white);box-shadow:0 4px 14px rgba(30,60,110,.12)"></div>

  <svg class="arrow" style="left:124px;top:2842px" width="20" height="32" viewBox="0 0 20 32"><path d="M17 2 L3 16 L17 30" fill="none" stroke="#b0b6bd" stroke-width="2.5"/></svg>
  <svg class="arrow" style="left:1027px;top:2842px" width="20" height="32" viewBox="0 0 20 32"><path d="M3 2 L17 16 L3 30" fill="none" stroke="#b0b6bd" stroke-width="2.5"/></svg>

  <div class="dl-shadow" style="left:168px;top:2780px"></div>
  <div class="dl-card" style="left:177px">
    <div class="doc" role="img" aria-label="Cover of a teal presentation document" style="background:linear-gradient(160deg,#2b8f95,#1d5d68)"></div>
    <h4>Presentations Title</h4>
    <p>Maecenas aliquet velit vel turpis Mauris neque metus malesuada nec ultricies sit amet porttitor mattis enim</p>
    <a class="btn">DOWNLOAD</a>
  </div>

  <div class="dl-shadow" style="left:596px;top:2780px"></div>
  <div class="dl-card" style="left:605px">
    <div class="doc" role="img" aria-label="Cover of an orange business brochure" style="background:linear-gradient(160deg,#f2b33a,#e7862b)"></div>
    <h4>Presentations Title</h4>
    <p>Maecenas aliquet velit vel turpis Mauris neque metus malesuada nec ultricies sit amet porttitor mattis enim</p>
    <a class="btn">DOWNLOAD</a>
  </div>
</section>

<footer class="footer">
  <div class="f-col" style="left:186px"><h5>COMPANY</h5><ul><li>Home</li><li>About Us</li><li>Why Us</li></ul></div>
  <div class="f-col" style="left:352px"><h5>WHY US</h5><ul><li>Our Services</li><li>Team</li><li>Blogs</li></ul></div>
  <div class="f-col" style="left:518px"><h5>RESOURCES</h5><ul><li>Download</li><li>Testimonials</li><li>Contact Us</li></ul></div>
  <div class="f-col" style="left:696px"><h5>CONTACT US</h5><ul>
    <li><svg width="13" height="13" viewBox="0 0 24 24"><path d="M6 2 L10 2 L11 7 L8 9 a13 13 0 0 0 7 7 L17 13 L22 14 L22 18 a3 3 0 0 1 -3 3 A17 17 0 0 1 3 5 a3 3 0 0 1 3 -3 Z" fill="#fff"/></svg>(420) 555 0187</li>
    <li><svg width="14" height="11" viewBox="0 0 24 18"><rect x="1" y="1" width="22" height="16" fill="#fff"/><path d="M1 1 L12 10 L23 1" fill="none" stroke="#1a5fc8" stroke-width="2"/></svg>info@kovrilex.com</li>
  </ul></div>
  <div class="f-col" style="left:911px"><h5>FOLLOW US</h5><ul>
    <li><svg width="12" height="12"><circle cx="6" cy="6" r="5" fill="#fff"/></svg>Chirper</li>
    <li><svg width="12" height="12"><circle cx="6" cy="6" r="5" fill="#fff"/></svg>Facepage</li>
    <li><svg width="12" height="12"><circle cx="6" cy="6" r="5" fill="#fff"/></svg>Linkwork</li>
  </ul></div>
</footer>
<div class="f-bar">© 2018 Kovrilex&nbsp; All right reserved</div>

</body>
</html>
```